New Business Card/Website Logo

We need a business card design for a new company based in Sydney. The company focuses mainly in construction in the field of form work and concreting. Attached is the logo being used already which can be used as a base for a new design, the current one is simply too bland and we are looking to spruce it up so it stands out and looks nicer. The logo would also be used on the website which is currently under construction. The attached image has the name, mobile and also the license number which needs to be there. The current email address on there can be removed and can be replaced with the website http://www.pillarvane.com.au, thanks!
Updates

Target Market(s)

Construction industry. Focusing on form work and concreting

Industry/Entity Type

Construction

Requirements
Must have
• License # on card along with website http://www.pillarvane.com.au and mobile phone number
Nice to have
• You have freedom with the design. The current design was a mock up done quite quickly. Please just keep in mind the target audience - construction, thanks.
Should not have
• the breezepost email address can be removed(refer picture) and replaced somewhere on the design with the website http://www.pillarvane.com.au

```html
<!DOCTYPE html>
<html lang="en">
<head>
<meta charset="utf-8">
<title>Pillarvane Business Card</title>
<link rel="stylesheet" href="https://fonts.googleapis.com/css2?family=Montserrat:wght@400;500&display=swap">
<style>
  :root {
    --card-yellow: #f2d82e;
    --ink-grey: #3e3e40;
    --band-white: #ffffff;
  }
  html, body {
    margin: 0;
    padding: 0;
    width: 1200px;
    height: 778px;
    overflow: hidden;
    background: var(--card-yellow);
  }
  .business-card {
    display: block;
    width: 1200px;
    height: 778px;
  }
  .card-background { fill: var(--card-yellow); }
  .name-band-stop-clear { stop-color: var(--band-white); stop-opacity: 0; }
  .name-band-stop-solid { stop-color: var(--band-white); stop-opacity: 1; }
  .company-name {
    font-family: "Montserrat", sans-serif;
    font-weight: 500;
    font-size: 108px;
    letter-spacing: 1px;
    fill: var(--ink-grey);
  }
  .contact-line {
    font-family: "Montserrat", sans-serif;
    font-weight: 400;
    font-size: 43px;
    fill: var(--ink-grey);
  }
  .contact-divider {
    stroke: var(--ink-grey);
    stroke-width: 3;
  }
</style>
</head>
<body>
  <svg class="business-card" viewBox="0 0 1200 778" xmlns="http://www.w3.org/2000/svg">
    <defs>
      <linearGradient id="name-band-fade" x1="0" y1="0" x2="1" y2="0">
        <stop offset="0" class="name-band-stop-clear"/>
        <stop offset="0.11" class="name-band-stop-solid"/>
        <stop offset="1" class="name-band-stop-solid"/>
      </linearGradient>
    </defs>

    <rect class="card-background" x="0" y="0" width="1200" height="778"/>

    <rect class="name-band" x="0" y="269" width="972" height="110" fill="url(#name-band-fade)"/>
    <text class="company-name" x="195" y="360">PILLARVANE</text>

    <text class="contact-line licence-number" x="197" y="456">Licence: 384512c</text>
    <text class="contact-line website" x="197" y="523">http://www.pillarvane.com.au</text>
    <line class="contact-divider" x1="197" y1="566" x2="677" y2="566"/>
    <text class="contact-line phone-number" x="197" y="653">Ph: 0412 578903</text>
  </svg>
</body>
</html>
```